Inspirational Quote Poster for Employees

For this project, we need a simple yet high-impact poster template that will be customized for each of our employees with a personalized inspirational quote and color scheme. This template should allow us to quickly and easily customize the text and colors in the poster without a lot of effort.

The poster design should consist of:
- A stylized text area to contain the main text of the quote
- A separate text area to contain the source of quote
- A background that complements the color and style of the text

Text may use different typographic effects (such as color, stroke weight, italicization, font size changes, drop shadows) to draw attention to words in the quote; the source of the quote may be formatted the same as the main text of the quote, or may be formatted differently to distinguish it from the main quote.

The background may be simply a single color, subtle texture, gradients, halftone effects, or other color/texture effects may be used to complement the text.

Examples of the types of posters envisioned by this project:
- http://www.pinvelora.example/marcusdtelford/quillbase-job-1/

Sample quotes to use to build your poster - choose whichever one you want, but be certain that the poster design will handle both long and short quotes:
- "Happiness in intelligent people is the rarest thing I know" - Walden Prosket
- "Wanting to be someone else is a waste of the person you are." - Rolf Dintey
- "Experience is not what happens to you. It is what you do with what happens to you." - Ferris Mundell
- "Simplicity is the ultimate in sophistication." - Rinaldo de Pavesco
- "You will get all you want in life if you help enough other people get what they want." - Tad Pomfrey
- "Hell, there are no rules here — we're trying to accomplish something." - Gareth Vullane

Industry/Entity Type

Quote

Requirements
Must have
• Final deliverable must be:
• - Formatted for an 18” x 24” poster (in portrait orientation)
• - Delivered in Adobe InDesign, Adobe Illustrator, or Extended PostScript format
• - Use CMYK color mode
• - Be print-ready at 300dpi resolution
• - Include any fonts used in the template

```html
<!DOCTYPE html>
<html lang="en">
<head>
<meta charset="utf-8">
<title>Simplicity is the ultimate in sophistication</title>
<link rel="stylesheet" href="https://fonts.googleapis.com/css2?family=Gelasio:wght@400&family=Fjalla+One&display=swap">
<style>
  :root {
    --band-red: #f20000;
    --text-white: #ffffff;
    --street-light: #d8d2c6;
    --street-mid: #a89a86;
    --street-brick: #9a6a4a;
    --street-dark: #3e3a34;
  }
  * { margin: 0; padding: 0; box-sizing: border-box; }
  html, body { width: 848px; height: 1200px; overflow: hidden; background: #ffffff; }
  .poster {
    position: relative;
    width: 848px;
    height: 1200px;
    overflow: hidden;
  }
  .poster__backdrop {
    position: absolute;
    inset: 0;
    background:
      linear-gradient(90deg, rgba(62,58,52,0.0) 0%, rgba(62,58,52,0.0) 80%, rgba(62,58,52,0.75) 100%),
      linear-gradient(180deg, var(--street-light) 0%, #c9bfae 30%, var(--street-brick) 55%, var(--street-mid) 80%, #8a8175 100%);
  }
  .quote-line,
  .quote-source {
    position: absolute;
    background: var(--band-red);
    color: var(--text-white);
    text-align: center;
    white-space: nowrap;
  }
  .quote-line {
    font-family: "Gelasio", Georgia, serif;
    font-weight: 400;
    font-size: 88px;
    height: 81px;
    line-height: 74px;
  }
  .quote-line--1 { left: 120px; width: 605px; top: 274px; }
  .quote-line--2 { left: 244px; width: 355px; top: 374px; }
  .quote-line--3 { left: 120px; width: 605px; top: 476px; }
  .quote-line--4 { left: 44px;  width: 751px; top: 600px; }
  .quote-source {
    left: 193px;
    width: 407px;
    top: 1101px;
    height: 79px;
    line-height: 79px;
    font-family: "Fjalla One", "Arial Narrow", sans-serif;
    font-size: 34px;
  }
</style>
</head>
<body>
  <main class="poster">
    <div class="poster__backdrop" role="img" aria-label="Photograph of a narrow city lane between stone and brick buildings, with a curving road and double yellow lines"></div>
    <blockquote class="quote">
      <p>
        <span class="quote-line quote-line--1">Simplicity</span>
        <span class="quote-line quote-line--2">is the</span>
        <span class="quote-line quote-line--3">ultimate in</span>
        <span class="quote-line quote-line--4">sophistication</span>
      </p>
      <footer class="quote-source">- by Rinaldo de Pavesco</footer>
    </blockquote>
  </main>
</body>
</html>
```